Business Card Design

I am selling Cruelty Free/not tested on animal products.
Ideally I would like pictures of rabbits/guinea pigs/Beagle(dog)/rat/mice, as these are the main creatures that are tested on.
Background of card Earth, clouds or rainbow.
Yes I am an animal activist.
My favorite colours are purple and green.

Reason: havent got the perfect design as yet

Industry/Entity Type

Business

Contact Information for Business Card

GENTLY BY NATURE
Cruelty Free Products
Norma Faldt
0492 837 514

```html
<!DOCTYPE html>
<html lang="en">
<head>
<meta charset="utf-8">
<title>Gently By Nature – Business Card</title>
<link rel="stylesheet" href="https://fonts.googleapis.com/css2?family=Alfa+Slab+One&family=Arimo:wght@400&display=swap">
<style>
  :root {
    --backdrop: #e9e7e3;
    --leaf: #8cc63f;
    --leaf-deep: #7bb531;
    --leaf-pale: #e4f1c6;
    --violet: #6a2a8e;
    --ink: #3a3a3a;
    --ribbon-pink: #f0648c;
    --ribbon-gold: #f6c945;
    --ribbon-sky: #4fc3e8;
    --ribbon-teal: #5fd1c2;
    --ribbon-white: #ffffff;
  }
  * { box-sizing: border-box; margin: 0; padding: 0; }
  html, body { width: 1200px; height: 725px; overflow: hidden; }
  body {
    position: relative;
    background: var(--backdrop);
    font-family: "Arimo", Arial, sans-serif;
  }
  .card {
    position: absolute;
    overflow: hidden;
    box-shadow: 0 4px 14px rgba(0,0,0,0.25);
  }
  .card-front {
    left: 38px; top: 32px; width: 407px; height: 660px;
    background: linear-gradient(160deg, var(--leaf) 0%, var(--leaf-deep) 100%);
  }
  .card-back {
    left: 502px; top: 158px; width: 663px; height: 407px;
    background: radial-gradient(ellipse at 30% 15%, var(--leaf-pale) 0%, #c2e08a 50%, var(--leaf) 100%);
  }
  .ribbons { position: absolute; inset: 0; width: 100%; height: 100%; }
  .brand-name {
    position: absolute;
    font-family: "Alfa Slab One", Georgia, serif;
    color: var(--violet);
    text-align: center;
    white-space: nowrap;
  }
  .animal-art {
    position: absolute;
    border-radius: 18px;
    background: radial-gradient(ellipse at center, rgba(106,42,142,0.28) 0%, rgba(106,42,142,0.08) 70%, rgba(106,42,142,0) 100%);
  }
  .tagline {
    position: absolute;
    font-family: "Alfa Slab One", Georgia, serif;
    color: var(--violet);
    text-align: center;
    white-space: nowrap;
    text-shadow: 2px 3px 3px rgba(0,0,0,0.25);
  }
  .card-front .brand-name { left: 0; width: 100%; top: 78px; font-size: 30px; }
  .card-front .animal-art { left: 72px; top: 122px; width: 290px; height: 218px; }
  .card-front .tagline { left: 0; width: 100%; top: 340px; font-size: 27px; }

  .card-back .brand-name { left: 40px; width: 340px; top: 52px; font-size: 26px; }
  .card-back .animal-art { left: 75px; top: 96px; width: 280px; height: 200px; }
  .card-back .tagline { left: 20px; width: 380px; top: 302px; font-size: 25px; }

  .holder { position: absolute; left: 396px; top: 152px; }
  .holder-name {
    font-family: "Alfa Slab One", Georgia, serif;
    color: var(--violet);
    font-size: 25px;
    line-height: 1.1;
  }
  .holder-role { color: var(--ink); font-size: 16px; margin-top: 4px; }
  .holder-phone {
    position: absolute; left: 482px; top: 226px;
    display: flex; align-items: center; gap: 10px;
    color: var(--ink); font-size: 17px; letter-spacing: 0.5px;
  }
  .holder-phone svg { width: 18px; height: 28px; }
</style>
</head>
<body>

  <section class="card card-front">
    <svg class="ribbons" viewBox="0 0 407 660" preserveAspectRatio="none" aria-hidden="true">
      <g fill="none" stroke-linecap="round">
        <path d="M-20 660 C 40 420, 20 200, 170 0" stroke="var(--ribbon-sky)" stroke-width="40" opacity="0.35"/>
        <path d="M10 660 C 60 420, 60 200, 220 -10" stroke="var(--ribbon-pink)" stroke-width="14" opacity="0.55"/>
        <path d="M40 660 C 80 450, 90 240, 260 -10" stroke="var(--ribbon-gold)" stroke-width="18" opacity="0.5"/>
        <path d="M80 660 C 110 470, 130 300, 320 0" stroke="var(--ribbon-teal)" stroke-width="26" opacity="0.3"/>
        <path d="M120 660 C 150 520, 220 420, 407 330" stroke="var(--ribbon-white)" stroke-width="3" opacity="0.55"/>
        <path d="M60 660 C 120 560, 260 520, 407 580" stroke="var(--ribbon-white)" stroke-width="2" opacity="0.45"/>
        <path d="M0 640 C 100 600, 250 640, 407 630" stroke="var(--ribbon-sky)" stroke-width="30" opacity="0.35"/>
      </g>
    </svg>
    <div class="brand-name">GENTLY BY NATURE</div>
    <div class="animal-art" role="img" aria-label="Purple line illustration of a guinea pig, a sitting beagle, a rabbit and a rat"></div>
    <div class="tagline">Cruelty Free Products</div>
  </section>

  <section class="card card-back">
    <svg class="ribbons" viewBox="0 0 663 407" preserveAspectRatio="none" aria-hidden="true">
      <g fill="none" stroke-linecap="round">
        <path d="M0 330 C 200 360, 450 330, 663 260" stroke="var(--ribbon-sky)" stroke-width="16" opacity="0.4"/>
        <path d="M0 360 C 220 385, 460 350, 663 290" stroke="var(--ribbon-teal)" stroke-width="14" opacity="0.5"/>
        <path d="M0 382 C 230 392, 470 360, 663 300" stroke="var(--ribbon-pink)" stroke-width="6" opacity="0.75"/>
        <path d="M0 392 C 240 400, 480 372, 663 318" stroke="var(--ribbon-gold)" stroke-width="6" opacity="0.7"/>
        <path d="M0 400 C 250 407, 500 392, 663 370" stroke="var(--ribbon-sky)" stroke-width="10" opacity="0.4"/>
        <path d="M0 345 C 210 372, 455 340, 663 276" stroke="var(--ribbon-white)" stroke-width="2" opacity="0.7"/>
      </g>
    </svg>
    <div class="brand-name">GENTLY BY NATURE</div>
    <div class="animal-art" role="img" aria-label="Purple line illustration of a guinea pig, a sitting beagle, a rabbit and a rat"></div>
    <div class="tagline">Cruelty Free Products</div>

    <div class="holder">
      <div class="holder-name">Norma Faldt</div>
      <div class="holder-role">Animal Activist</div>
    </div>
    <div class="holder-phone">
      <svg viewBox="0 0 18 28" aria-hidden="true">
        <rect x="1" y="1" width="16" height="26" rx="3" fill="none" stroke="var(--ink)" stroke-width="2"/>
        <rect x="4" y="5" width="10" height="15" fill="var(--ink)"/>
        <circle cx="9" cy="23.5" r="1.5" fill="var(--ink)"/>
      </svg>
      <span>0492 837 514</span>
    </div>
  </section>

</body>
</html>
```